Flyer for family counseling

For my family counseling I'm looking for a design for flyers. Important is not only the appearance of the flyer, but also the content design. All important contents can be found on my website: www.brigitte-volkanter.at The following items should NOT appear on the flyer: - constellation work - bereavement and palliative work My logo should definitely be on the flyer. Source files are available.

Target Market(s)

Families, individuals, children, couples in need of psychological support.

Colors

Designer to choose colors to be used in the design.

Requirements
Must have
• My logo - source files available Website and contact data Recognition value from website to flyer and vice versa
Should not have
• Mention of the constellation work and mourning and palliative work not desired.

```html
<!DOCTYPE html>
<html lang="en">
<head>
<meta charset="utf-8">
<title>Family Counseling Flyer</title>
<link href="https://fonts.googleapis.com/css2?family=Cinzel:wght@500;700&family=Montserrat:wght@400;600;700&display=swap" rel="stylesheet">
<style>
:root{
  --navy:#1f3f8f;
  --teal:#1e9e97;
  --blue:#1f78c1;
  --ink:#4a4f57;
  --footer:#3a3f46;
  --bg:#e9e7e3;
  --paper:#ffffff;
}
*{box-sizing:border-box;margin:0;padding:0}
html,body{width:1200px;height:754px;overflow:hidden;background:var(--bg)}
body{font-family:'Montserrat',sans-serif;color:var(--ink);position:relative}
.page{position:absolute;top:12px;width:520px;height:730px;background:var(--paper);overflow:hidden;box-shadow:0 2px 10px rgba(0,0,0,.15)}
.page--front{left:50px}
.page--back{left:630px}
.abs{position:absolute}
.photo{position:absolute;border-radius:10px;overflow:hidden}
.photo__label{position:absolute;left:0;bottom:10px;background:var(--teal);color:#fff;font-size:8px;font-weight:700;letter-spacing:1px;padding:4px 10px;border-radius:0 8px 8px 0;text-transform:uppercase}
.hero{position:absolute;right:0;top:0;width:300px;height:215px;background:linear-gradient(135deg,#dfe9ee,#c9b8a5 55%,#5b7fa8);border-bottom-left-radius:40px}
.brand{position:absolute;left:40px;top:58px;display:flex;align-items:center;gap:8px}
.brand__mark{width:24px;height:24px;border-radius:50%;background:var(--teal)}
.brand__name{font-size:10px;font-weight:700;color:var(--navy);letter-spacing:1px;line-height:1.2}
.brand__sub{display:block;font-size:6px;letter-spacing:2px;font-weight:600}
.headline{position:absolute;left:40px;top:108px;width:190px;font-family:'Cinzel',serif;font-weight:700;font-size:15px;line-height:1.15;color:var(--navy)}
.ticks{list-style:none}
.ticks li{position:relative;padding-left:12px;font-size:7px;line-height:1.45;margin-bottom:1px}
.ticks li::before{content:"";position:absolute;left:0;top:2px;width:7px;height:7px;border-radius:50%;background:var(--teal)}
.ticks li::after{content:"";position:absolute;left:2.3px;top:3.3px;width:2px;height:3.4px;border:solid #fff;border-width:0 1px 1px 0;transform:rotate(45deg)}
.ticks--bold li{font-weight:700;color:var(--navy);font-size:7.5px}
.rule{position:absolute;left:0;top:226px;width:100%;height:2px;background:var(--teal)}
h3{font-size:9px;font-weight:700;color:var(--navy);margin:6px 0 4px}
p{font-size:7px;line-height:1.45;margin-bottom:5px}
.col{position:absolute}
.contact-tab{position:absolute;right:0;top:648px;background:var(--blue);color:#fff;font-weight:700;font-size:11px;padding:8px 22px;border-top-left-radius:18px;display:flex;align-items:center;gap:6px}
.footer{position:absolute;left:0;bottom:0;width:100%;height:40px;background:var(--footer);color:#fff;font-size:7.5px;display:flex;align-items:center;gap:24px;padding:0 22px;border-top:4px solid var(--blue)}
.footer span{display:flex;align-items:center;gap:5px}
.panel{position:absolute;left:20px;top:250px;width:250px;height:385px;background:var(--teal);border-radius:0 0 12px 0;color:#fff;padding:30px 14px 10px}
.panel__title{position:absolute;left:0;top:0;background:var(--navy);color:#fff;font-size:8px;font-weight:700;letter-spacing:1px;padding:5px 12px}
.portrait{position:absolute;right:14px;top:-34px;width:56px;height:56px;border-radius:50%;border:3px solid #fff;background:linear-gradient(#f2d9c4,#c64b3f)}
.timeline{list-style:none}
.timeline li{font-size:6.6px;line-height:1.35;margin-bottom:4px;padding-left:8px;position:relative}
.timeline li::before{content:"";position:absolute;left:0;top:3px;width:3px;height:3px;border-radius:50%;background:#fff}
.timeline b{display:block;font-size:7px}
.voices{border-top:1px solid var(--blue);padding-top:6px;margin-top:4px}
.voices h3{color:var(--blue);letter-spacing:1px}
.voices__who{text-align:right;font-size:6.5px;color:var(--blue);font-style:italic;margin-bottom:5px}
</style>
</head>
<body>

<!-- FRONT -->
<section class="page page--front">
  <div class="hero" role="img" aria-label="Photo of a family with a baby talking with a counselor on a sofa"></div>
  <div class="brand">
    <div class="brand__mark"></div>
    <div class="brand__name">BRIGITTE VOLKANTER<span class="brand__sub">FAMILIENBERATUNG WIEN</span></div>
  </div>
  <h1 class="headline">Has your life reached a point where change is needed?</h1>
  <ul class="ticks abs" style="left:40px;top:180px;width:190px">
    <li>Accompanying people in their development</li>
    <li>Attention, clear view and empathy</li>
    <li>A calm, personal approach to change</li>
  </ul>
  <div class="rule"></div>

  <div class="photo" style="left:26px;top:240px;width:225px;height:130px;background:linear-gradient(135deg,#efe4d6,#b79b86)" role="img" aria-label="Photo of a counseling room with an armchair and a client">
    <div class="photo__label">Individual counseling</div>
  </div>
  <div class="photo" style="left:270px;top:240px;width:225px;height:130px;background:linear-gradient(135deg,#dfe8cf,#c9a27d)" role="img" aria-label="Photo of a counselor reading a picture book with two children">
    <div class="photo__label">Child guidance</div>
  </div>

  <div class="col" style="left:26px;top:378px;width:225px">
    <h3>Unauthorized from the crisis</h3>
    <ul class="ticks ticks--bold">
      <li>Is it enough for you?</li>
      <li>Has a point been reached where nothing works?</li>
      <li>Is the time ripe for change?</li>
    </ul>
    <p style="margin-top:5px">There are ways out of the impasse. Let yourself be guided to find them. Once taken, the path is your own.</p>
    <p>For the very personal way to self-determination, personal development becomes a wonderful adventure.</p>
    <h3>The individual advice helps:</h3>
    <ul class="ticks">
      <li>to regain more positive views</li>
      <li>yes to say to yourself and to accept it better</li>
      <li>to change conflict patterns</li>
      <li>to gain more self-confidence</li>
      <li>change negative behavior</li>
      <li>make room for yourself and the positive things in life</li>
      <li>solve your problems on your own responsibility</li>
      <li>take a new attitude to yourself and others</li>
      <li>regain access to your blocked resources</li>
    </ul>
  </div>

  <div class="col" style="left:270px;top:378px;width:225px">
    <h3>Guide – lead – accompany</h3>
    <h3 style="margin-top:0">Court-ordered family, parenting or educational counseling according to § 107 Abs. 3 Z 1 AußStrG</h3>
    <p>In the case of non-functioning custody and contact regulations or disagreement between parents, the court may order counseling. I support you in finding solutions that serve the well-being of your children.</p>
    <p>My job is to assist you in a trusting environment, to find a new form of parental cooperation and to focus your attention on the needs of the child.</p>
    <h3>Out-of-court education advice</h3>
    <p>Children are a wonderful gift. And a big challenge. Sometimes we need help from the outside to meet again lovingly and with mutual respect.</p>
    <p>My most important school is my life and work. In my practice I have learned to deal with very different problems. One result was always the same: there is always a solution, whether we are dealing with behavioral problems or learning disabilities.</p>
  </div>

  <div class="contact-tab">
    <svg width="10" height="10" viewBox="0 0 24 24"><path fill="#fff" d="M6.6 10.8a15 15 0 0 0 6.6 6.6l2.2-2.2c.3-.3.7-.4 1-.2 1.1.4 2.3.6 3.6.6.6 0 1 .4 1 1V20c0 .6-.4 1-1 1A17 17 0 0 1 3 4c0-.6.4-1 1-1h3.5c.6 0 1 .4 1 1 0 1.3.2 2.5.6 3.6.1.3 0 .7-.2 1z"/></svg>
    +43 660 418 27 59
  </div>
  <footer class="footer">
    <span><svg width="8" height="10" viewBox="0 0 24 30"><path fill="#fff" d="M12 0a10 10 0 0 0-10 10c0 8 10 20 10 20s10-12 10-20A10 10 0 0 0 12 0zm0 14a4 4 0 1 1 0-8 4 4 0 0 1 0 8z"/></svg>Lindengasse 14/3, 1070 Vienna</span>
    <span><svg width="10" height="8" viewBox="0 0 24 18"><rect x="1" y="1" width="22" height="16" fill="none" stroke="#fff" stroke-width="2"/><path d="M1 1l11 9 11-9" fill="none" stroke="#fff" stroke-width="2"/></svg>familienberatung@brigitte-volkanter.at</span>
  </footer>
</section>

<!-- BACK -->
<section class="page page--back">
  <div class="photo" style="left:20px;top:22px;width:230px;height:120px;background:linear-gradient(135deg,#efe6d8,#a88d78)" role="img" aria-label="Photo of a couple in a counseling session with the counselor">
    <div class="photo__label">Couples counseling</div>
  </div>
  <div class="photo" style="left:270px;top:22px;width:230px;height:120px;background:linear-gradient(135deg,#e4ead6,#9e8a7a)" role="img" aria-label="Photo of a family with children sitting together in a counseling room">
    <div class="photo__label">Family &amp; children</div>
  </div>

  <div class="col" style="left:20px;top:150px;width:230px">
    <h3>Basis and new beginning</h3>
    <p>Marital or partnership problems – always the same topics or situations, the feeling of being in a circle.</p>
    <p>Patterns can be resolved. I would like to support you on your way to a new start as a couple or to venture a respectful new beginning.</p>
  </div>

  <div class="panel">
    <div class="panel__title">Professional background</div>
    <div class="portrait" role="img" aria-label="Portrait photo of the counselor"></div>
    <ul class="timeline">
      <li><b>December 2017</b>Course: Basic trauma management</li>
      <li><b>April 2017</b>Certificate: Counselor in accordance with § 107 AußStrG</li>
      <li><b>November 2016</b>Education: Motivational short intervention</li>
      <li><b>October 2015</b>Training: Hypnosystemic counseling for anxiety disorders</li>
      <li><b>May 2015</b>Training: Systemic work with couples in motion</li>
      <li><b>January 2015</b>Course: Life, loss and grief counseling basics</li>
      <li><b>November 2014</b>Interdisciplinary symposium: Couples in transition</li>
      <li><b>October 2013</b>Qualification for the counseling of parents according to § 95 Abs. 1a AußStrG</li>
      <li><b>June 2012</b>Seminar: Nonviolent communication</li>
      <li><b>November 2011</b>Diploma in systemic installation management</li>
      <li><b>October 2010</b>Training: Experience-oriented development for children</li>
      <li><b>May 2009</b>Training: Developmental psychology and general psychology</li>
      <li><b>April 2008</b>Training: Conflict psychology and methodology</li>
      <li><b>June 2006</b>Education: Systemic life and social counselor</li>
    </ul>
  </div>

  <div class="col" style="left:270px;top:150px;width:230px">
    <h3>Living together</h3>
    <h3 style="margin-top:0">What is a family counseling and how does it work?</h3>
    <p>In family counseling every single member of the family is heard and taken seriously. Together we look at patterns, roles and needs, and develop new ways of living together that suit everyone.</p>
    <p>After the goal has been defined jointly, the focus is on the strengths and resources of the family as a whole.</p>
    <h3>Themes of a family counseling</h3>
    <p>Children are a wonderful gift. And a big challenge. Sometimes we need help from the outside to meet again lovingly and with mutual respect.</p>
    <p>My most important school is my life and work. In my practice I have learned to deal with very different problems. One result was always the same: there is always a solution.</p>
    <h3>The individual advice helps:</h3>
    <ul class="ticks">
      <li>Life crises, such as separation or serious illness</li>
      <li>Problems at school, with friends or in the family</li>
      <li>Behavioral problems of a child, such as ADHD or school refusal</li>
    </ul>
    <div class="voices">
      <h3>VOICES OF CLIENTS:</h3>
      <p>Brigitte Volkanter is characterized by warmth, sympathy, calm and care. Safe and loving, she accompanies you through the process. You feel welcomed and taken care of.</p>
      <div class="voices__who">Mrs. R., client</div>
      <p>My way was full of stones and wood. I took the broom in the hand and returned. Mrs. Volkanter accompanied me.</p>
      <div class="voices__who">Mrs. H., client</div>
    </div>
  </div>

  <div class="contact-tab">
    <svg width="10" height="10" viewBox="0 0 24 24"><path fill="#fff" d="M6.6 10.8a15 15 0 0 0 6.6 6.6l2.2-2.2c.3-.3.7-.4 1-.2 1.1.4 2.3.6 3.6.6.6 0 1 .4 1 1V20c0 .6-.4 1-1 1A17 17 0 0 1 3 4c0-.6.4-1 1-1h3.5c.6 0 1 .4 1 1 0 1.3.2 2.5.6 3.6.1.3 0 .7-.2 1z"/></svg>
    +43 660 418 27 59
  </div>
  <footer class="footer">
    <span><svg width="8" height="10" viewBox="0 0 24 30"><path fill="#fff" d="M12 0a10 10 0 0 0-10 10c0 8 10 20 10 20s10-12 10-20A10 10 0 0 0 12 0zm0 14a4 4 0 1 1 0-8 4 4 0 0 1 0 8z"/></svg>Lindengasse 14/3, 1070 Vienna</span>
    <span><svg width="10" height="8" viewBox="0 0 24 18"><rect x="1" y="1" width="22" height="16" fill="none" stroke="#fff" stroke-width="2"/><path d="M1 1l11 9 11-9" fill="none" stroke="#fff" stroke-width="2"/></svg>familienberatung@brigitte-volkanter.at</span>
  </footer>
</section>

</body>
</html>
```